Professional, Attractive, Simple Website Needed!!

We completed the design for our logo.

We need a website built out around this.

Here are a couple samples of how we want ours formatted.

http://brvntapower.com

http://www.halvorbeam.com/lp/free-quote?LeadSource=Search%20Engine&ProgramName=webquery&experience=qual&language=en&type=brd&gclid=Xq7RTPwmEYKDLAvUHbsNQkfPZrTcGwnJuoVbXeLqHmRYdAsWtPkMcNfBYgzTrUoQJhEdWvKpYaLsZbCmNDgQwTxAoKpXbT_qkR

http://morvalo.co

Reason: Extending this deadline due to our delay in providing designers with content for each page. This is coming in next 24 hours.

Reason: Due to scheduling conflicts and extended travel delays related to Puerto Rico, the deadline has been extended. Your patience is greatly appreciated.

Reason: Travel and scheduling conflicts have made it impossible to give this project the thorough review it deserves, therefore I am extending the deadline. Thank you for your patience!

Target Market(s)

Home Owners who earn 60k + household annually

Industry/Entity Type

It Professional

Coding

Coded - Design and coding required

Number of Pages Required

5+ page

Font styles to use
Serif

Colors
34a7d8
9bcb3c

Requirements
Must have
• Simple
• Lead form Entry (Ability for visitor to enter Name, number and address for a quote)
• Sleek Design
• Professional
• Testimonials
• Use color Scheme of Design Logo Attached
Nice to have
• Video when site starts
• Like this
• https://www.vidmarrow.com/watch?v=qT8mRpXw2Ka&feature=vidm.ro
Should not have
• Should not include Commercial solar
• Should not include wind power

```html
<!DOCTYPE html>
<html lang="en">
<head>
<meta charset="utf-8">
<title>Contact Us — Clear Horizon Energy</title>
<link href="https://fonts.googleapis.com/css2?family=Roboto:wght@400;500&display=swap" rel="stylesheet">
<style>
:root{
  --brand-blue:#34a7d8;
  --brand-green:#9bcb3c;
  --ink:#1f1f1f;
  --ink-soft:#333;
  --white:#ffffff;
  --hero-top:#2f4560;
  --hero-mid:#3c5673;
  --hero-low:#4b5563;
  --footer-top:#3a3f46;
  --footer-low:#25324a;
  --footer-bar:#232629;
  --rule:#222;
}
*{margin:0;padding:0;box-sizing:border-box}
html,body{width:1200px;height:814px;overflow:hidden;background:var(--white)}
body{position:relative;font-family:"Roboto",Arial,sans-serif;color:var(--ink)}

.hero{position:absolute;left:0;top:0;width:1200px;height:187px;
  background:linear-gradient(180deg,var(--hero-top) 0%,var(--hero-mid) 55%,var(--hero-low) 100%)}
.hero-photo{position:absolute;inset:0}
.nav-rule{position:absolute;left:0;top:69px;width:1200px;height:1px;background:rgba(255,255,255,.75)}
.nav a{position:absolute;top:53px;font-size:9px;letter-spacing:.2px;color:var(--white);text-decoration:none;text-transform:uppercase}
.brand{position:absolute;display:flex;flex-direction:column;align-items:center;color:var(--brand-blue);font-weight:500;text-align:center}
.brand-dot{border-radius:50%;border:2px solid var(--brand-blue)}
.brand-name{font-size:10px;line-height:1.1;margin-top:3px;letter-spacing:.3px}
.hero-title{position:absolute;left:0;width:1200px;top:112px;text-align:center;color:var(--white);font-size:22px;font-weight:400;letter-spacing:.3px}

.contact-list{position:absolute;left:285px;top:264px}
.contact-row{position:absolute;left:0;display:flex;align-items:flex-start;gap:6px;font-size:12px;white-space:nowrap;color:var(--ink)}
.contact-row svg{flex:none}
.social-label{position:absolute;left:285px;top:364px;font-size:11.5px}
.social-icons{position:absolute;left:287px;top:388px;display:flex;gap:16px}
.social-icon{width:17px;height:17px;border:1.4px solid #666;border-radius:50%}
.map-link{position:absolute;left:285px;top:417px;font-size:11.5px;color:var(--ink);text-decoration:underline}

.lead-form{position:absolute;left:646px;top:214px;width:250px}
.form-title{text-align:center;font-size:12px;margin-bottom:0}
.field{position:absolute;left:0;width:250px;border-bottom:1.5px solid var(--rule);font-size:11.5px;padding:0 0 6px 8px;color:var(--ink)}
.send{position:absolute;left:74px;top:289px;width:100px;height:25px;border:2px solid var(--rule);background:var(--white);font-family:inherit;font-size:11.5px;color:var(--ink)}

.footer{position:absolute;left:0;top:560px;width:1200px;height:254px;
  clip-path:polygon(0 37%,50% 0,100% 37%,100% 100%,0 100%);
  background:linear-gradient(180deg,var(--footer-top) 0%,#343c48 45%,var(--footer-low) 100%)}
.footer-photo{position:absolute;inset:0}
.footer-contacts .contact-row{color:var(--white);font-size:11.5px}
.follow{position:absolute;left:711px;top:692px;font-size:11px;color:var(--white);letter-spacing:.2px}
.footer-icons{position:absolute;left:707px;top:714px;display:flex;gap:12px}
.footer-icons .social-icon{border-color:#ddd;width:16px;height:16px}
.footer-bar{position:absolute;left:0;top:783px;width:1200px;height:31px;background:var(--footer-bar);color:var(--white);font-size:7px;text-align:center;line-height:31px}
</style>
</head>
<body>

<header class="hero">
  <div class="hero-photo" role="img" aria-label="Photo looking up a tall glass office tower against a blue sky"></div>
  <nav class="nav">
    <a href="#" style="left:348px">Home</a>
    <a href="#" style="left:412px">About us</a>
    <a href="#" style="left:490px">Services</a>
    <a href="#" style="left:670px">Gallery</a>
    <a href="#" style="left:744px">FAQ</a>
    <a href="#" style="left:799px">Contact us</a>
  </nav>
  <div class="brand" style="left:549px;top:10px;width:100px">
    <span class="brand-dot" style="width:30px;height:30px"></span>
    <span class="brand-name">Clear Horizon Energy</span>
  </div>
  <div class="nav-rule"></div>
  <h1 class="hero-title">CONTACT US</h1>
</header>

<main>
  <section class="contact-list">
    <div class="contact-row" style="top:1px">
      <svg width="12" height="14" viewBox="0 0 12 14"><path d="M6 13s-4.6-4.6-4.6-7.6a4.6 4.6 0 0 1 9.2 0C10.6 8.4 6 13 6 13z" fill="none" stroke="#333" stroke-width="1.1"/><circle cx="6" cy="5.4" r="1.7" fill="none" stroke="#333" stroke-width="1.1"/></svg>
      <span>Kharkiv, Linden Street 27</span>
    </div>
    <div class="contact-row" style="top:27px">
      <svg width="15" height="12" viewBox="0 0 15 12"><rect x="1" y="1.5" width="13" height="9" fill="none" stroke="#333" stroke-width="1.1"/><path d="M1 1.5l6.5 5.5 6.5-5.5M1 10.5l4.8-4.2M14 10.5l-4.8-4.2" fill="none" stroke="#333" stroke-width="1"/></svg>
      <span>m.serdiuk@postline.net</span>
    </div>
    <div class="contact-row" style="top:51px">
      <svg width="15" height="15" viewBox="0 0 15 15"><path d="M3 1.5l2.4 2.7-1.3 1.6c.9 2 2.5 3.6 4.5 4.5l1.6-1.3 2.7 2.4-1.6 2c-5.5-.6-9.5-4.6-10.1-10.1z" fill="none" stroke="#333" stroke-width="1.1"/><path d="M9 1.5a4.5 4.5 0 0 1 4.5 4.5M9 3.8a2.2 2.2 0 0 1 2.2 2.2" fill="none" stroke="#333" stroke-width="1"/></svg>
      <span>+38(050)612-40-18<br>+38(050)612-40-19</span>
    </div>
  </section>
  <p class="social-label">We are in social networks:</p>
  <div class="social-icons">
    <span class="social-icon" aria-label="Social network link"></span>
    <span class="social-icon" aria-label="Social network link"></span>
    <span class="social-icon" aria-label="Social network link"></span>
  </div>
  <a class="map-link" href="#">Search us on the map</a>

  <form class="lead-form">
    <p class="form-title">Have questions? Fill the form!</p>
    <div class="field" style="top:44px">Name</div>
    <div class="field" style="top:92px">Phone</div>
    <div class="field" style="top:140px">Email</div>
    <div class="field" style="top:235px">Message</div>
    <button class="send" type="button">SEND</button>
  </form>
</main>

<footer>
  <div class="footer">
    <div class="footer-photo" role="img" aria-label="Photo of dark solar panels under the sky"></div>
  </div>
  <div class="brand" style="left:549px;top:590px;width:100px">
    <span class="brand-dot" style="width:30px;height:30px"></span>
    <span class="brand-name">Clear Horizon Energy</span>
  </div>
  <section class="contact-list footer-contacts" style="left:426px;top:671px">
    <div class="contact-row" style="top:1px">
      <svg width="12" height="14" viewBox="0 0 12 14"><path d="M6 13s-4.6-4.6-4.6-7.6a4.6 4.6 0 0 1 9.2 0C10.6 8.4 6 13 6 13z" fill="none" stroke="#fff" stroke-width="1.1"/><circle cx="6" cy="5.4" r="1.7" fill="none" stroke="#fff" stroke-width="1.1"/></svg>
      <span>Kharkiv, Ukraine</span>
    </div>
    <div class="contact-row" style="top:26px">
      <svg width="15" height="12" viewBox="0 0 15 12"><rect x="1" y="1.5" width="13" height="9" fill="none" stroke="#fff" stroke-width="1.1"/><path d="M1 1.5l6.5 5.5 6.5-5.5M1 10.5l4.8-4.2M14 10.5l-4.8-4.2" fill="none" stroke="#fff" stroke-width="1"/></svg>
      <span>m.serdiuk@postline.net</span>
    </div>
    <div class="contact-row" style="top:50px">
      <svg width="15" height="15" viewBox="0 0 15 15"><path d="M3 1.5l2.4 2.7-1.3 1.6c.9 2 2.5 3.6 4.5 4.5l1.6-1.3 2.7 2.4-1.6 2c-5.5-.6-9.5-4.6-10.1-10.1z" fill="none" stroke="#fff" stroke-width="1.1"/><path d="M9 1.5a4.5 4.5 0 0 1 4.5 4.5M9 3.8a2.2 2.2 0 0 1 2.2 2.2" fill="none" stroke="#fff" stroke-width="1"/></svg>
      <span>+38(050)612-40-18<br>+38(050)612-40-19</span>
    </div>
  </section>
  <p class="follow">FOLLOW US</p>
  <div class="footer-icons">
    <span class="social-icon" aria-label="Social network link"></span>
    <span class="social-icon" aria-label="Social network link"></span>
    <span class="social-icon" aria-label="Social network link"></span>
  </div>
  <div class="footer-bar">© 2017 Clear Horizon Energy. All Rights Reserved</div>
</footer>

</body>
</html>
```